Etiketten für eine Apotherflasche
Zielgruppe
Wir sind eine Familienbrennerei aus Karlsruhe-Bulach, die von Vater und Tochter geführt wird. Wir stellen Edeldestillate, Whiskys, Gins und Liköre in Handarbeit her und legen großen Wert auf die Verwendung regionaler Rohstoffe, hauptsächlich von unseren eigenen Streuobstwiesen.
Aufgabenstellung
Wir benötigen ein Flaschenetikett für eine klassische Apotherflasche 0,5 Liter.
Der Inhalt wird unser 'Feldmarer Gin' sein.
Das Etikett sollte auf jeden Fall den Produktnamen 'Feldmarer Gin' enthalten.
Es wäre schön, wenn das Desgin die Stadt Karlsruhe wiederspiegeln würde - z.B. Fächer (da Fächerstadt), Stadtkarte im Hintergrund, Pyramide (Wahrzeichen von Karlsruhe) - hier dürfen Sie gerne kreativ werden.
Informationen zu uns bzw. unserer Brennerei finden Sie unter www.valdenhof-brennerei.de.
Bitte nicht an den dort existierenden Etiketten orientieren - diese werden akteuell umgestellt.
Maße des Etiketts sollten ca. 95x85mm sein.
Wir freuen uns auf die

```html
<!DOCTYPE html>
<html lang="de">
<head>
<meta charset="utf-8">
<title>Feldmarer Gin – Etikett</title>
<link rel="stylesheet" href="https://fonts.googleapis.com/css2?family=Lato:wght@900&display=swap">
<style>
  :root {
    --paper: #ffffff;
    --ink: #1d1d1b;
    --map-light: #8a8a88;
    --map-dark: #3a3a38;
  }
  html, body {
    margin: 0;
    padding: 0;
    width: 1200px;
    height: 1163px;
    overflow: hidden;
    background: var(--paper);
  }
  .label {
    position: absolute;
    left: 150px;
    top: 131px;
    width: 900px;
    height: 900px;
  }
  .label svg { display: block; width: 100%; height: 100%; }
  .product-city {
    font-family: "Lato", Arial, sans-serif;
    font-weight: 900;
    fill: var(--ink);
  }
  .product-type {
    font-family: "Lato", Arial, sans-serif;
    font-weight: 900;
    fill: var(--ink);
  }
  .corner-edge {
    stroke: var(--ink);
    stroke-width: 6;
    stroke-linecap: butt;
  }
</style>
</head>
<body>
  <main class="label">
    <svg viewBox="0 0 928 928" xmlns="http://www.w3.org/2000/svg">
      <defs>
        <linearGradient id="map-tone" x1="0" y1="0" x2="1" y2="1">
          <stop offset="0" stop-color="var(--map-light)"/>
          <stop offset="1" stop-color="var(--map-dark)"/>
        </linearGradient>
      </defs>

      <g class="corner-map" role="img" aria-label="Stadtplan-Ausschnitt in Schwarz-Weiß, obere linke Ecke">
        <polygon points="0,0 278,0 0,278" fill="url(#map-tone)"/>
      </g>
      <g class="corner-map" role="img" aria-label="Stadtplan-Ausschnitt in Schwarz-Weiß, obere rechte Ecke">
        <polygon points="650,0 928,0 928,278" fill="url(#map-tone)"/>
      </g>
      <g class="corner-map" role="img" aria-label="Stadtplan-Ausschnitt in Schwarz-Weiß, untere linke Ecke">
        <polygon points="0,650 0,928 278,928" fill="url(#map-tone)"/>
      </g>
      <g class="corner-map" role="img" aria-label="Stadtplan-Ausschnitt in Schwarz-Weiß, untere rechte Ecke">
        <polygon points="928,650 928,928 650,928" fill="url(#map-tone)"/>
      </g>

      <line class="corner-edge" x1="278" y1="0" x2="0" y2="278"/>
      <line class="corner-edge" x1="650" y1="0" x2="928" y2="278"/>
      <line class="corner-edge" x1="0" y1="650" x2="278" y2="928"/>
      <line class="corner-edge" x1="928" y1="650" x2="650" y2="928"/>

      <text class="product-city" x="118" y="338" font-size="96"
            textLength="697" lengthAdjust="spacingAndGlyphs">FELDMARER</text>
      <text class="product-type" x="118" y="680" font-size="403"
            textLength="697" lengthAdjust="spacingAndGlyphs">GIN</text>
    </svg>
  </main>
</body>
</html>
```